Healthy Supplement featuring Moringa products

Need 3 business card options for our reps to order from Cardloom. Our reps will be ordering from Cardloom once we upload them. Attached is our current designs to show what info needs to be on the cards. Our website is www.tkvitality.com
The business cards will be a template for our reps to order from. Most of our reps are Asian & Hispanic. Please look at our website so you can see who we are to get the look and feel what we need.
Target Market(s)
Adults 30 on up. Health oriented people.
Industry/Entity Type
Health And Wellness
Contact Information for Business Card
Name
Title
Phone
Logo
www.tkvitality.com/my/username
Font styles to use
Requirements
Must have
- Please match our website look and colors. A moringa leaf is nice, but am open to something different.
Nice to have
- Healthy looking and warm, not super cold or too modern.
Should not have
- No harsh colors please.

```html
<!DOCTYPE html>
<html lang="en">
<head>
<meta charset="UTF-8">
<title>TK Vitality — Business Card</title>
<link rel="stylesheet" href="https://fonts.googleapis.com/css2?family=Cinzel:wght@400&family=Lato:wght@400&display=swap">
<style>
  :root {
    --bg: #e4e4e4;
    --green-dark: #5aa512;
    --green-mid: #7cc11d;
    --green-light: #9fd33a;
    --leaf-deep: #3f9a2a;
    --leaf-soft: #6fbb3c;
    --lime-band: #a9d63f;
    --brand-green: #6db21f;
    --text-dark: #333333;
    --rule-orange: #f2a33a;
    --white: #ffffff;
  }
  * { margin: 0; padding: 0; box-sizing: border-box; }
  html, body { width: 1200px; height: 900px; overflow: hidden; }
  body {
    background: var(--bg);
    position: relative;
    font-family: "Lato", Arial, sans-serif;
  }
  .card {
    position: absolute;
    width: 560px;
    height: 320px;
    border-radius: 22px;
    overflow: hidden;
    box-shadow: 0 10px 24px rgba(0,0,0,0.18);
  }
  /* Front */
  .card-front {
    left: 80px; top: 110px;
    background: linear-gradient(160deg, var(--green-dark) 0%, var(--green-mid) 55%, var(--green-light) 100%);
  }
  .front-foliage {
    position: absolute;
    left: 40px; top: 20px;
    width: 300px; height: 300px;
    border-radius: 50% 40% 0 0;
    background: radial-gradient(ellipse at 50% 55%, rgba(255,255,255,0.18) 0%, rgba(255,255,255,0.06) 60%, rgba(255,255,255,0) 75%);
  }
  .front-brand {
    position: absolute;
    left: 0; right: 0; top: 132px;
    text-align: center;
    font-family: "Cinzel", Georgia, serif;
    font-size: 40px;
    letter-spacing: 4px;
    color: var(--white);
  }
  /* Back */
  .card-back {
    left: 560px; top: 470px;
    background: var(--white);
  }
  .back-band {
    position: absolute;
    left: 0; top: 0; bottom: 0;
    width: 200px;
    background: var(--lime-band);
    clip-path: polygon(0 30%, 78% 0, 100% 0, 100% 100%, 0 100%);
  }
  .back-foliage {
    position: absolute;
    left: 0; top: 20px; bottom: 0;
    width: 250px;
    background: linear-gradient(150deg, var(--leaf-soft) 0%, var(--leaf-deep) 60%, var(--leaf-soft) 100%);
    clip-path: polygon(0 35%, 70% 0, 100% 20%, 92% 100%, 0 100%);
  }
  .back-brand {
    position: absolute;
    right: 34px; top: 34px;
    font-family: "Cinzel", Georgia, serif;
    font-size: 26px;
    letter-spacing: 3px;
    color: var(--brand-green);
  }
  .rep {
    position: absolute;
    left: 282px; top: 128px;
    width: 250px;
  }
  .rep-name {
    font-family: "Cinzel", Georgia, serif;
    font-size: 19px;
    color: var(--brand-green);
    letter-spacing: 1px;
  }
  .rep-title {
    font-size: 14px;
    color: var(--text-dark);
    margin-top: 1px;
  }
  .rep-rule {
    height: 1.5px;
    background: var(--rule-orange);
    margin: 9px 0 10px;
  }
  .contact-list { list-style: none; }
  .contact-item {
    display: flex;
    align-items: center;
    gap: 7px;
    font-size: 14px;
    color: var(--text-dark);
    line-height: 21px;
    white-space: nowrap;
  }
  .contact-icon { width: 12px; height: 12px; flex: none; }
</style>
</head>
<body>
  <section class="card card-front">
    <div class="front-foliage" role="img" aria-label="Faint moringa leaf sprig in the background"></div>
    <div class="front-brand">TK VITALITY</div>
  </section>

  <section class="card card-back">
    <div class="back-band"></div>
    <div class="back-foliage" role="img" aria-label="Photograph of fresh moringa leaf sprigs"></div>
    <div class="back-brand">TK VITALITY</div>
    <div class="rep">
      <div class="rep-name">DANIEL REYES</div>
      <div class="rep-title">Managing Director</div>
      <div class="rep-rule"></div>
      <ul class="contact-list">
        <li class="contact-item">
          <svg class="contact-icon" viewBox="0 0 12 12"><path d="M1 3c0-1 1-2 2-2l1 2-1 1c.6 1.6 2 3 3.5 3.5l1-1 2 1c0 1-1 2-2 2C4.5 9.5 1 6 1 3z" fill="var(--brand-green)"/></svg>
          <span>044-555 019 274</span>
        </li>
        <li class="contact-item">
          <svg class="contact-icon" viewBox="0 0 12 12"><rect x="0.5" y="2.5" width="11" height="7.5" fill="var(--brand-green)"/><path d="M0.5 2.5 6 7l5.5-4.5" stroke="#fff" fill="none" stroke-width="1"/></svg>
          <span>hello@tkvitality.com</span>
        </li>
        <li class="contact-item">
          <svg class="contact-icon" viewBox="0 0 12 12"><circle cx="6" cy="6" r="5.5" fill="var(--brand-green)"/><path d="M0.5 6h11M6 0.5c-2.5 3-2.5 8 0 11M6 0.5c2.5 3 2.5 8 0 11" stroke="#fff" fill="none" stroke-width="0.8"/></svg>
          <span>www.tkvitality.com/my/username</span>
        </li>
      </ul>
    </div>
  </section>
</body>
</html>
```